Custom Label for Women's Supplement Brand

Need a product label for our products, we have a logo designed but need to incorporate it in to our product line which will have capsule bottles, tincture bottles, and eventually skin care. We originally wanted a label that had black as main color, but are open to options. Want it to be sleek, and pull the eye, simple yet fun. Even something different that doesn’t look like anyone else.
Updates

Low designer entries

Target Market(s)

Women 26-70

Requirements
Nice to have
• Would love some metallic accents

```html
<!DOCTYPE html>
<html lang="en">
<head>
<meta charset="utf-8">
<title>Even Keel Health – Supplement Label</title>
<link href="https://fonts.googleapis.com/css2?family=Poppins:wght@500;600;700;800&display=swap" rel="stylesheet">
<style>
  :root {
    --backdrop: #bdbdbd;
    --label-black: #121212;
    --label-black-soft: #1e1e1e;
    --brand-green: #9cc243;
    --accent-blue: #29c4e6;
    --metal-orange: #c97a26;
    --text-white: #f4f4f4;
    --tab-ink: #151515;
  }
  * { box-sizing: border-box; margin: 0; padding: 0; }
  html, body {
    width: 1200px;
    height: 891px;
    overflow: hidden;
    background: var(--backdrop);
    font-family: "Poppins", sans-serif;
  }
  .canvas {
    position: relative;
    width: 1200px;
    height: 891px;
  }
  .label {
    position: absolute;
    left: 150px;
    top: 18px;
    width: 900px;
    height: 855px;
    background: radial-gradient(ellipse at 50% 40%, var(--label-black-soft) 0%, var(--label-black) 70%);
    overflow: hidden;
  }
  .brand {
    position: absolute;
    top: 150px;
    left: 0;
    width: 100%;
    display: flex;
    justify-content: center;
    align-items: center;
    gap: 16px;
  }
  .brand-dot {
    width: 30px;
    height: 30px;
    border-radius: 50%;
    background: var(--brand-green);
  }
  .brand-name {
    font-weight: 600;
    font-size: 46px;
    color: var(--brand-green);
    letter-spacing: 0.5px;
  }
  .product-name {
    position: absolute;
    top: 335px;
    left: 0;
    width: 100%;
    text-align: center;
    font-weight: 700;
    font-size: 128px;
    line-height: 104px;
    color: var(--metal-orange);
    text-shadow: 3px 6px 8px rgba(0, 0, 0, 0.75);
  }
  .tagline {
    position: absolute;
    top: 584px;
    left: 0;
    width: 100%;
    text-align: center;
    font-weight: 500;
    font-size: 19.5px;
    line-height: 24px;
    color: var(--text-white);
    letter-spacing: -0.2px;
  }
  .category {
    position: absolute;
    top: 786px;
    left: 210px;
    font-weight: 700;
    font-size: 12px;
    letter-spacing: 9.5px;
    color: var(--text-white);
  }
  .stripe-blue {
    position: absolute;
    left: 0;
    top: 814px;
    width: 100%;
    height: 5px;
    background: var(--accent-blue);
  }
  .band-green {
    position: absolute;
    left: 0;
    top: 825px;
    width: 100%;
    height: 30px;
    background: var(--brand-green);
  }
  .count-tab {
    position: absolute;
    left: 665px;
    top: 723px;
    width: 140px;
    height: 132px;
    background: var(--brand-green);
    border-radius: 52px 52px 0 0;
    text-align: center;
    color: var(--tab-ink);
  }
  .count-number {
    display: block;
    margin-top: 14px;
    font-weight: 800;
    font-size: 64px;
    line-height: 64px;
  }
  .count-unit {
    display: block;
    font-weight: 600;
    font-size: 16px;
    line-height: 18px;
  }
</style>
</head>
<body>
  <main class="canvas">
    <section class="label">
      <div class="brand">
        <span class="brand-dot"></span>
        <span class="brand-name">Even Keel Health</span>
      </div>

      <h1 class="product-name">PRODUCT<br>NAME</h1>

      <p class="tagline">Lorem ipsum dolor sit amet, consectetur adipiscing elit,<br>sed do eiusmod tempor incididunt ut labore</p>

      <p class="category">HEALTH SUPPLEMENT</p>

      <div class="stripe-blue"></div>
      <div class="band-green"></div>

      <div class="count-tab">
        <span class="count-number">30</span>
        <span class="count-unit">CAPSULES</span>
      </div>
    </section>
  </main>
</body>
</html>
```